Amber Moth Glen- Luxury Tree-house Wellness Resort Website

Amber Moth Glen is a luxury nature wellness resort. Please look at our current website for content information and aesthetic. Brand
ing, imaging and color pallet all stay the same. We need the website simplified and easier to understand and better flow visually. More use of videos. I can send additional photos or videos. I love whimsical and magical. We don’t need to add extra content.
We have a vintage storybook theme with rich woods, alligator leather, nautical compasses, ship wheel, we have skeleton keys to miniature doors. Think Tobias under the hill. The concept is for the guest to stay and enjoy their time. Not travel to see other things. No fishing, no excursions. All on site, animals, gardens, games, meditation tools, relaxing and recharging. Again, please keep the same text and pictures that’s on the website now. I like adding as many slow videos as possible

Target Market(s)

Luxury Travelers. Wealthy Tourists.

Industry/Entity Type

Luxury Nature and Wellness Resort

Coding

Coded - Design and coding required

Number of Pages Required

4 page

Font styles to use
Serif
Script

Requirements
Must have
• All the photos and descriptions that are currently on the website. videos in the background. motion, textures
Nice to have
• Please ADD More pictures of the people/experience. I would like to have a textured background and maybe a palm leaf that is stationary in the lower right corner of the website that stays still while you scroll.

```html
<!DOCTYPE html>
<html lang="en">
<head>
<meta charset="utf-8">
<title>Amber Moth Glen — Luxury Campground Resort</title>
<link rel="stylesheet" href="https://fonts.googleapis.com/css2?family=Playfair+Display:wght@400;600;700&family=Montserrat:wght@400;500;600&display=swap">
<style>
:root{
  --bark:#3b3029;
  --bark-deep:#2f2620;
  --card:#4a3e35;
  --gold:#ecd68c;
  --cream:#f1df92;
  --ink:#2e251f;
  --text-light:#f3ead2;
  --muted:#cbbf9f;
}
*{box-sizing:border-box;margin:0;padding:0}
html,body{width:1200px;height:2548px;overflow:hidden;background:var(--bark)}
body{font-family:"Montserrat",sans-serif;color:var(--text-light);position:relative}

/* Hero */
.hero{position:absolute;left:0;top:0;width:1200px;height:600px}
.hero-photo{position:absolute;inset:0;background:
  radial-gradient(ellipse at 60% 55%,rgba(214,150,60,.55),transparent 55%),
  linear-gradient(180deg,#2b3a2e 0%,#4a4030 45%,#6b5130 70%,#3b3029 100%)}
.nav{position:absolute;top:0;left:0;width:1200px;height:110px}
.nav-pill{position:absolute;top:14px;background:var(--gold);color:var(--ink);font-size:11px;font-weight:500;padding:7px 22px;border-radius:20px}
.brand{position:absolute;top:12px;left:50%;transform:translateX(-50%);text-align:center;background:rgba(59,48,41,.85);width:130px;height:86px;padding-top:14px;border-radius:0 0 8px 8px}
.brand-dot{width:26px;height:26px;border-radius:50%;border:2px solid var(--gold);margin:0 auto 6px}
.brand-name{font-family:"Playfair Display",serif;font-size:13px;color:var(--gold);letter-spacing:1px;line-height:1.1}
.hero-copy{position:absolute;top:290px;width:1200px;text-align:center}
.hero-copy h1{font-family:"Playfair Display",serif;font-weight:700;font-size:46px;color:#fff7e0}
.hero-copy p{font-family:"Playfair Display",serif;font-size:24px;line-height:32px;margin-top:12px;color:#fff3d6}
.btn{display:inline-block;margin-top:76px;background:var(--gold);color:var(--ink);font-weight:600;font-size:14px;padding:12px 28px;border-radius:4px}

/* Section headings */
.heading{position:absolute;left:0;width:1200px;display:flex;justify-content:center;align-items:center;gap:18px}
.heading h2{font-family:"Playfair Display",serif;font-weight:600;font-size:46px;color:var(--gold)}
.heading .mark{width:44px;height:44px;border-radius:50%;border:2px solid var(--gold)}

/* Accommodations */
.stay-card{position:absolute;top:808px;width:400px;height:480px;background:var(--card)}
.stay-photo{height:276px}
.stay-body{padding:34px 30px}
.stay-body h3{font-family:"Playfair Display",serif;font-size:22px;color:var(--gold);margin-bottom:16px}
.bullets{list-style:none;font-size:11.5px;line-height:22px;color:var(--text-light)}
.bullets li::before{content:"• ";color:var(--gold)}
.cols{display:flex;gap:22px}

/* Packages */
.pkg{position:absolute;top:1500px;width:256px;height:222px;background:var(--card);padding:24px 24px}
.pkg-top{display:flex;align-items:center;gap:16px;margin-bottom:10px}
.pkg-icon{width:60px;height:60px;border-radius:50%;background:var(--cream);display:flex;align-items:center;justify-content:center;flex:none}
.pkg h3{font-family:"Playfair Display",serif;font-size:18px;color:var(--gold)}
.pkg .bullets{font-size:10.5px;line-height:19px}

/* Reunions */
.cream{position:absolute;top:1790px;left:0;width:1200px;height:480px;background:var(--cream)}
.circle-photo{position:absolute;left:280px;top:1840px;width:270px;height:270px;border-radius:50%;
  background:radial-gradient(circle at 50% 45%,#a8773c,#6b4a2a 70%,#4a3424)}
.reunion-copy{position:absolute;left:580px;top:1900px;width:360px;color:var(--ink)}
.reunion-copy h2{font-family:"Playfair Display",serif;font-weight:600;font-size:46px;line-height:48px}
.reunion-copy p{font-size:10.5px;line-height:16px;margin-top:18px}

/* Contact */
.contact{position:absolute;top:2280px;width:1200px;text-align:center}
.contact .heading{position:static}
.contact .heading h2{font-size:30px}
.contact .heading .mark{width:30px;height:30px}
.contact p{font-size:10px;line-height:16px;color:var(--muted)}
.contact .lead{margin:6px 0 14px;color:var(--text-light)}
.contact .copy{margin-top:12px}
</style>
</head>
<body>

<header class="hero">
  <div class="hero-photo" role="img" aria-label="Photo of illuminated treehouse cabins among mossy oaks at dusk"></div>
  <nav class="nav">
    <span class="nav-pill" style="left:280px">Home</span>
    <span class="nav-pill" style="left:372px">Accommodations</span>
    <div class="brand"><div class="brand-dot"></div><div class="brand-name">AMBER MOTH<br>GLEN</div></div>
    <span class="nav-pill" style="left:680px">Packages</span>
    <span class="nav-pill" style="left:784px">Contact</span>
  </nav>
  <div class="hero-copy">
    <h1>Luxury Campground Resort</h1>
    <p>Elevated treehouses, curated surprises<br>&amp; unforgettable gatherings</p>
    <span class="btn">Plan Your Adventure</span>
  </div>
</header>

<svg style="position:absolute;left:0;top:560px" width="1200" height="60" aria-hidden="true">
  <polygon fill="var(--bark)" points="0,30 60,22 120,34 190,20 260,32 330,24 400,36 470,22 540,30 620,20 700,34 780,24 860,32 940,20 1020,30 1100,22 1200,30 1200,60 0,60"/>
</svg>

<div class="heading" style="top:712px"><span class="mark"></span><h2>Accommodations</h2></div>

<article class="stay-card" style="left:180px">
  <div class="stay-photo" role="img" aria-label="Photo of the main house at night with lit deck and fire pit" style="background:linear-gradient(160deg,#2a2520,#6a4a2a 55%,#3a2a20)"></div>
  <div class="stay-body">
    <h3>Main House – Bartholomew</h3>
    <div class="cols">
      <ul class="bullets"><li>Hosts 17 Guests</li><li>Hot Tub &amp; BBQ</li><li>Chef's Kitchen</li></ul>
      <ul class="bullets"><li>Hidden Treasure Rooms</li><li>Mini Golf &amp; Swings</li><li>5 Bedrooms &amp; 5 Bunk Beds</li></ul>
    </div>
  </div>
</article>
<article class="stay-card" style="left:620px">
  <div class="stay-photo" role="img" aria-label="Photo of a tree-house tent among tall oaks and greenery" style="background:linear-gradient(160deg,#5b6a4a,#8a7a55 50%,#4a4030)"></div>
  <div class="stay-body">
    <h3>Luxury Tree-house Tents</h3>
    <ul class="bullets"><li>Custom-curated items on check-in</li><li>Serene natural setting &amp; ultimate privacy</li><li>Fully climate-controlled &amp; tile bathrooms</li></ul>
  </div>
</article>

<svg style="position:absolute;left:0;top:1310px" width="1200" height="40" aria-hidden="true">
  <polygon fill="var(--bark-deep)" points="0,20 80,12 150,24 230,10 310,22 400,14 480,26 560,12 650,22 740,10 820,24 900,14 990,22 1080,12 1200,20 1200,40 0,40"/>
</svg>

<div class="heading" style="top:1380px"><span class="mark"></span><h2>Packages &amp; Experiences</h2></div>

<article class="pkg" style="left:172px">
  <div class="pkg-top"><span class="pkg-icon"><svg width="26" height="26" viewBox="0 0 26 26"><path d="M8 3v8a3 3 0 0 0 6 0V3M11 3v20M19 3c-3 2-3 8 0 10v10" fill="none" stroke="var(--ink)" stroke-width="2"/></svg></span><h3>Culinary</h3></div>
  <ul class="bullets"><li>Private Chef Option</li><li>Fresh Local Seafood</li><li>S'mores &amp; Firepits</li><li>BBQ Grilling</li><li>Farm-to-Table</li></ul>
</article>
<article class="pkg" style="left:472px">
  <div class="pkg-top"><span class="pkg-icon"><svg width="26" height="26" viewBox="0 0 26 26"><circle cx="13" cy="13" r="10" fill="none" stroke="var(--ink)" stroke-width="2"/><path d="M13 6l3 7-3 7-3-7z" fill="var(--ink)"/></svg></span><h3>Adventure</h3></div>
  <ul class="bullets"><li>Wildlife Viewing</li><li>Garden Wanderings</li><li>Campfire Building</li><li>Treasure Hunts</li><li>Arts &amp; Crafts</li></ul>
</article>
<article class="pkg" style="left:772px">
  <div class="pkg-top"><span class="pkg-icon"><svg width="26" height="26" viewBox="0 0 26 26"><path d="M13 22c-6-4-8-9-8-13 4 0 7 3 8 6 1-3 4-6 8-6 0 4-2 9-8 13z" fill="none" stroke="var(--ink)" stroke-width="2"/></svg></span><h3>Relaxation</h3></div>
  <ul class="bullets"><li>Natural Immersion</li><li>Meditation Tools &amp; Yoga</li><li>Bird Watching</li><li>Aromatherapy</li><li>Soothing Sounds</li></ul>
</article>

<section class="cream"></section>
<svg style="position:absolute;left:0;top:1760px" width="1200" height="40" aria-hidden="true">
  <polygon fill="var(--cream)" points="0,24 70,14 140,28 220,10 300,26 380,16 460,30 540,12 620,26 700,14 790,28 870,12 950,24 1040,14 1120,26 1200,16 1200,40 0,40"/>
</svg>
<div class="circle-photo" role="img" aria-label="Photo of guests gathered in a warmly lit tree-house lounge"></div>
<div class="reunion-copy">
  <h2>Reunions<br>&amp; Retreats</h2>
  <p>Private family reunions, birthday parties and milestone celebrations, treasure hunts and quiet wellness retreats — every curated gathering happens without ever leaving our property. Our tree-house resort is your storybook hideaway for making memories together, slow mornings and starlit evenings.</p>
</div>
<svg style="position:absolute;left:0;top:2240px" width="1200" height="40" aria-hidden="true">
  <polygon fill="var(--bark)" points="0,18 90,10 170,24 250,8 340,22 420,12 510,26 600,10 690,22 770,12 860,26 950,10 1040,22 1120,12 1200,20 1200,40 0,40"/>
</svg>

<footer class="contact">
  <div class="heading"><span class="mark"></span><h2>Contact &amp; Reservations</h2></div>
  <p class="lead">Begin your storybook adventure today. Disconnect to connect.</p>
  <p>Phone: (555) 014-2280</p>
  <p>Email: stay@ambermothglen.example</p>
  <p>Address: 1402 Lantern Hollow Road, Willowmere, GA 31000</p>
  <p class="copy">© 2024 Amber Moth Glen. All Rights Reserved.</p>
</footer>

</body>
</html>
```